Business Card Design Harbor of Calm

mental health provider
contemporary
warmth
inviting

Target Market(s)

mental health clients adults

Industry/Entity Type

Mental Health

Contact Information for Business Card

Danielle Arkwright PMHNP
2841 SW Tenley Ave
Suite 384C
Portland OR 97318
Fax 503-555-0182
Tel 503-555-0147
Email danielle@darkwright.example
Website darkwright.example

Requirements
Nice to have
• see above
Should not have
• no medical logos

```html
<!DOCTYPE html>
<html lang="en">
<head>
<meta charset="UTF-8">
<title>Harbor of Calm — Business Card</title>
<link rel="stylesheet" href="https://fonts.googleapis.com/css2?family=Roboto:wght@400;500;700&display=swap">
<style>
  :root {
    --backdrop: #1b1b1c;
    --card: #2c2c2d;
    --accent: #3ec4f0;
    --ink: #f1f1f1;
    --ink-soft: #d6d6d6;
  }
  * { box-sizing: border-box; margin: 0; padding: 0; }
  html, body {
    width: 1200px;
    height: 900px;
    overflow: hidden;
    background: var(--backdrop);
    font-family: "Roboto", Arial, sans-serif;
    color: var(--ink);
  }
  .stage {
    width: 1200px;
    height: 900px;
    display: flex;
    flex-direction: column;
    align-items: center;
    justify-content: center;
    gap: 60px;
  }
  .card {
    position: relative;
    width: 620px;
    height: 354px;
    background: var(--card);
    box-shadow: 0 10px 30px rgba(0,0,0,0.45);
  }

  /* Front */
  .identity {
    position: absolute;
    left: 52px;
    top: 70px;
  }
  .identity__name {
    font-size: 26px;
    font-weight: 700;
    letter-spacing: 0.3px;
    text-transform: uppercase;
    line-height: 1;
  }
  .identity__title {
    display: inline-block;
    margin-top: 6px;
    font-size: 12px;
    letter-spacing: 0.6px;
    color: var(--ink-soft);
    padding-bottom: 3px;
    border-bottom: 2px solid var(--accent);
  }
  .address-rule {
    position: absolute;
    left: 0;
    top: 128px;
    display: flex;
    align-items: center;
    gap: 12px;
  }
  .rule {
    display: block;
    height: 7px;
    background: var(--accent);
  }
  .address-rule .rule { width: 300px; }
  .address {
    font-size: 11px;
    color: var(--ink-soft);
    white-space: nowrap;
  }
  .contact {
    list-style: none;
    font-size: 11px;
    line-height: 1.6;
    color: var(--ink-soft);
  }
  .contact__label { color: var(--accent); }
  .contact--phone {
    position: absolute;
    left: 52px;
    top: 158px;
  }
  .contact--online {
    position: absolute;
    left: 400px;
    top: 282px;
  }
  .edge-stub {
    position: absolute;
    right: 0;
    top: 270px;
    width: 22px;
  }

  /* Back */
  .site-rule {
    position: absolute;
    left: 0;
    right: 0;
    top: 212px;
    display: flex;
    align-items: center;
    gap: 10px;
  }
  .site-rule .rule--long { width: 300px; }
  .site-rule .rule--short { flex: 1; }
  .site-rule__url {
    font-size: 13px;
    font-weight: 700;
    letter-spacing: 0.4px;
    white-space: nowrap;
  }
</style>
</head>
<body>
  <main class="stage">
    <section class="card card--front" aria-label="Business card front">
      <div class="identity">
        <h1 class="identity__name">Danielle Arkwright</h1>
        <p class="identity__title">PMHNP</p>
      </div>
      <div class="address-rule">
        <span class="rule"></span>
        <p class="address">2841 SW Tenley Ave Suite 384C Portland OR 97318</p>
      </div>
      <ul class="contact contact--phone">
        <li><span class="contact__label">fax:</span> 503-555-0182</li>
        <li><span class="contact__label">telephone:</span> 503-555-0147</li>
      </ul>
      <ul class="contact contact--online">
        <li><span class="contact__label">email:</span> danielle@darkwright.example</li>
        <li><span class="contact__label">website:</span> www.darkwright.example</li>
      </ul>
      <span class="rule edge-stub"></span>
    </section>

    <section class="card card--back" aria-label="Business card back">
      <div class="site-rule">
        <span class="rule rule--long"></span>
        <p class="site-rule__url">WWW.DARKWRIGHT.EXAMPLE</p>
        <span class="rule rule--short"></span>
      </div>
    </section>
  </main>
</body>
</html>
```